One page flyer for nonprofit focused IT company

I need a one page flyer (one side of a single 8.5x11 page) with text and graphics. The company logo is already done, and it must appear on the flyer along with other icons and graphics. The final design will be printed on heavy weight glossy paper as a handout and also distributed as a PDF.

The text is provided in an attachment, if it needs to be shortened let me know.

Industry/Entity Type

Information Technology

Requirements
Must have
• some flare (colors, icons or images)
Should not have
• While we work for nonprofits, my company is a FOR PROFIT company.

```html
<!DOCTYPE html>
<html lang="en">
<head>
<meta charset="utf-8">
<title>Meridian Systems – 50 Years of NonProfit IT Services</title>
<link rel="stylesheet" href="https://fonts.googleapis.com/css2?family=Fira+Sans:ital,wght@0,400;0,600;0,700;1,500;1,600&display=swap">
<style>
  :root {
    --maroon: #8e1b2b;
    --ink: #1a1a1a;
    --paper: #ffffff;
    --backdrop: #3f3f3f;
    --photo-deep: #0d1524;
    --photo-mid: #1f3552;
    --photo-glow: #4a6f99;
  }
  * { box-sizing: border-box; margin: 0; padding: 0; }
  html, body { width: 1200px; height: 849px; overflow: hidden; }
  body {
    background: var(--backdrop);
    font-family: "Fira Sans", sans-serif;
    color: var(--ink);
    position: relative;
  }
  .flyer {
    position: absolute;
    left: 280px; top: 10px;
    width: 640px; height: 829px;
    background: var(--paper);
    padding: 36px 37px 0 38px;
  }
  .masthead { display: flex; height: 104px; }
  .brand {
    width: 230px;
    display: flex; align-items: center; justify-content: center;
    gap: 10px; padding-top: 10px;
  }
  .brand-dot { width: 14px; height: 14px; border-radius: 50%; background: var(--maroon); flex: none; }
  .brand-name {
    font-weight: 600; color: var(--ink);
    font-size: 19px; line-height: 1.15;
  }
  .headline { margin-left: 7px; width: 292px; }
  .headline h1 {
    font-weight: 700; font-size: 28px; line-height: 29px;
    padding-bottom: 4px; border-bottom: 2px solid var(--ink);
    white-space: nowrap;
  }
  .headline p {
    margin-top: 6px; color: var(--maroon);
    font-style: italic; font-weight: 500; font-size: 13.5px; line-height: 16px;
  }
  .intro { margin-top: 6px; font-size: 10px; line-height: 12.6px; }
  .band {
    margin-top: 6px; height: 15px; background: var(--maroon); color: #fff;
    font-weight: 700; font-size: 11.5px; line-height: 15px; padding-left: 6px;
  }
  .columns { display: grid; grid-template-columns: repeat(3, 181px); column-gap: 11px; }
  .case { margin-top: 12px; }
  .case h3, .service h3 {
    color: var(--maroon); font-style: italic; font-weight: 600;
    font-size: 11.5px; line-height: 14px; margin-bottom: 4px;
  }
  .case p, .service p {
    font-size: 10px; line-height: 12.6px; text-align: justify; hyphens: auto;
  }
  .photo {
    margin-top: 5px; height: 173px; width: 566px;
    background:
      radial-gradient(ellipse at 78% 55%, #2b2b33 0 18%, transparent 40%),
      linear-gradient(90deg, var(--photo-deep) 0%, var(--photo-mid) 35%, var(--photo-glow) 55%, var(--photo-mid) 75%, var(--photo-deep) 100%);
  }
  .solutions { margin-top: 8px; }
  .service { margin-top: 12px; min-height: 100px; }
  .service .icon { float: right; width: 26px; height: 26px; margin: 4px 8px 2px 8px; }
  .service.row2 { margin-top: 0; }
</style>
</head>
<body>
  <article class="flyer">
    <header class="masthead">
      <div class="brand">
        <span class="brand-dot"></span>
        <div class="brand-name">Meridian Systems<br>Corporation</div>
      </div>
      <div class="headline">
        <h1>50 Years of<br>NonProfit IT Services</h1>
        <p>An Efficient and Elegant Approach to IT Solution Implementations</p>
      </div>
    </header>

    <p class="intro">Meridian Systems Corporation has been supporting the Information Systems needs of nonprofits for over 50 years. We continually strive to bring the latest technologies and best practices to nonprofits to drive down the cost of IT while implementing systems that drive revenue. Our Agile approach to IT management means that we deliver working systems to every one of our clients every two weeks.</p>

    <h2 class="band">Successes</h2>
    <section class="columns successes">
      <div class="case">
        <h3>90% Reduction in Software Development Costs</h3>
        <p>Halvorsen's National Auto Retailers Guild needed to update their core product offering; they engaged their in-house IT department who estimated the project would take 3 years at a cost of $3,000,000. NARG decided to work with Meridian Systems Corporation instead, and the product was released to production in only 9 months at one tenth of the cost, only $300,000</p>
      </div>
      <div class="case">
        <h3>10x Increase in Membership</h3>
        <p>Greenway Paths Alliance needed to move to online membership registration and contracted with Meridian Systems Corporation to build a significant online presence and engage potential members. Through compelling online tools and mobile applications Greenway Paths has increased membership 10 fold.</p>
      </div>
      <div class="case">
        <h3>20% Reduction in Overhead</h3>
        <p>The National Alliance for Civic Leaders had antiquated systems and processes in place to manage over 500 chapters across the nation. Working with MSC they implemented online tools to allow communication and management between the local chapters and national headquarters. This eliminated much of the overhead of chapter management, reducing HR costs by 20%.</p>
      </div>
    </section>

    <div class="photo" role="img" aria-label="Photo of an IT professional holding a laptop in a dimly lit server room"></div>

    <h2 class="band solutions">Solutions</h2>
    <section class="columns">
      <div class="service">
        <svg class="icon" viewBox="0 0 30 30" aria-hidden="true"><g fill="none" stroke="#111" stroke-width="2"><circle cx="15" cy="15" r="12.5"/><ellipse cx="15" cy="15" rx="5.5" ry="12.5"/><path d="M2.5 15h25M4.5 8.5h21M4.5 21.5h21M15 2.5v25"/></g></svg>
        <h3>Web Applications</h3>
        <p>With a focus on non-profit websites and web based applications, MSC helps nonprofits communicate with their members and donors while maximizing online giving and engagement.</p>
      </div>
      <div class="service">
        <svg class="icon" viewBox="0 0 30 30" aria-hidden="true"><rect x="8" y="1" width="14" height="28" rx="2" fill="#111"/><rect x="10" y="4" width="10" height="20" fill="#fff"/><path d="M11.5 22v-3h1.8v3zM14.2 22v-5h1.8v5zM16.9 22v-7h1.8v7z" fill="#111"/></svg>
        <h3>Mobile Applications</h3>
        <p>Meridian Systems Corporation implements mobile applications for Orbit and Nimbus to provide direct communications with members and donors enabling real-time, two way interaction.</p>
      </div>
      <div class="service">
        <svg class="icon" viewBox="0 0 30 30" aria-hidden="true"><circle cx="7" cy="7" r="4" fill="#111"/><path d="M1 25v-7a6 6 0 0 1 12 0v7z" fill="#111"/><rect x="13" y="11" width="16" height="12" fill="none" stroke="#111" stroke-width="1.8"/><circle cx="21" cy="17" r="2.5" fill="none" stroke="#111" stroke-width="1.5"/><path d="M10 25h19" stroke="#111" stroke-width="1.8"/></svg>
        <h3>Systems Integration</h3>
        <p>Every nonprofit's IT applications are scattered and disconnected. Meridian Systems Corporation has decades of experience integrating these applications into a single cohesive system.</p>
      </div>
      <div class="service row2">
        <svg class="icon" viewBox="0 0 30 30" aria-hidden="true"><path d="M2 1v27h27" fill="none" stroke="#111" stroke-width="2"/><path d="M4 22l5-8 4 5 5-9 4 4 5-9" fill="none" stroke="#111" stroke-width="1.8"/><path d="M5 17l5-4 4 4 5-6 3 2 5-5" fill="none" stroke="#111" stroke-width="1.2"/></svg>
        <h3>Business Intelligence and Reporting</h3>
        <p>Meridian Systems Corporation can wrestle all of an organization's data into simple executive dashboards and reports.</p>
      </div>
      <div class="service row2">
        <svg class="icon" viewBox="0 0 30 30" aria-hidden="true" fill="#111"><circle cx="15" cy="7" r="5"/><circle cx="6" cy="10" r="3.5"/><circle cx="24" cy="10" r="3.5"/><path d="M7 27a8 8 0 0 1 16 0z"/><path d="M0 24a6 6 0 0 1 9-5 10 10 0 0 0-3 5zM30 24a6 6 0 0 0-9-5 10 10 0 0 1 3 5z"/></svg>
        <h3>Member Donor Database</h3>
        <p>Meridian Systems Corporation's GiveLedger Member / Donor CRM system is fully customized for each client meeting the unique needs of your organization.</p>
      </div>
      <div class="service row2">
        <svg class="icon" viewBox="0 0 30 30" aria-hidden="true"><path d="M8 24a6 6 0 0 1-1-12 8 8 0 0 1 15-2 6.5 6.5 0 0 1 1 14z" fill="#111"/><circle cx="8" cy="12" r="5" fill="#fff" stroke="#111" stroke-width="1.5"/><path d="M5.5 12l2 2 3-4" fill="none" stroke="#111" stroke-width="1.5"/></svg>
        <h3>Cloud Migration</h3>
        <p>Reduce IT costs by migrating to the latest cloud solutions.</p>
      </div>
    </section>
  </article>
</body>
</html>
```